Türschildvorlagen mit Alternativfarben für ein Pflegeheim (Bewohnerzimmer & andere Räume)
Zielgruppe
Der Birkenau ist ein privates Alten- und Pflegeheim. Im Zuge von Umbaumaßnahmen sollen die Türschilder im Haus neu gestsltet werden. Die Türschilder hängen in einer Kunststoff-Halterung neben jeder Tür (Bewohnerzimmer, Funktionsräume etc.). (Siehe zur Veranschaulichung die angehängte Datei 'Beispielfoto Türschild.jpg). Die Gebäudeebenen sind farblich unterschiedlich gestaltet, was auch in den Türschildern aufgegriffen werden soll (siehe Aufgabenstellung).
Aufgabenstellung
Für die Türschildhalterungen soll eine optisch ansprechende Türschildvorlage erstellt werden. Die Vorlage muss folgende Kriterien erfüllen:
1. Exakte Maße der Vorlage: Breite: 14,8 cm, Höhe: 10,8 cm.
2. Inhalte:
a) Zimmernummer (3 oder 4-stellig)
b) Name des Bewohners / des Raumes
c) Grafikelement, das das Firmenlogo aufgreift (Nachträglicher Hinweis: Das Logo muss nicht 1 zu 1 übernommen werden sondern kann variiert werden als Designelement. Auch der BIRKENAU-Schriftzug kann entfallen!)
d) Farbcode für die jeweilige Gebäudeebene
==> Farben der Ebenen:
E0: Lichtgrün (RAL 6027, CMYK 60 0 30 0); E1: Narzissengelb (RAL 1007, CMYK 0 40 100 0); E2: Signalblau (RAL 5005, CMYK 100 40 0 40); E3: Verkehrsrot (RAL 3020, CMYK 0 100 100 10); E4: Wasserblau (RAL 5021, CMYK 100 20 50 10); E5: Signalorange (RAL 2010, CMYK 0 70 100 10); E6: Patinagrün (RAL 6000, CMYK 80 20 60 20)
3. Die Vorlage sollte möglichst einfach mit "handelsüblichen Programmen" (MS Word?) editiert werden können (Ändern Zimmernummer + Name).

```html
<!DOCTYPE html>
<html lang="de">
<head>
<meta charset="utf-8">
<title>Türschildvorlagen Birkenau – Ebenen E0 bis E6</title>
<link rel="stylesheet" href="https://fonts.googleapis.com/css2?family=PT+Sans+Narrow:wght@400;700&display=swap">
<style>
  :root {
    --page-bg: #ffffff;
    --brand-blue: #00478f;
    --text-dark: #111111;
    --number-text: #ffffff;

    --e0: #66c2bd; --e0-tint: #c0e3e0;
    --e1: #f5a500; --e1-tint: #fcd590;
    --e2: #005189; --e2-tint: #7d9fc8;
    --e3: #d0070f; --e3-tint: #e48a75;
    --e4: #007e7e; --e4-tint: #87b9bc;
    --e5: #db6006; --e5-tint: #eaa77a;
    --e6: #1e826a; --e6-tint: #a2bfb2;
  }

  * { margin: 0; padding: 0; box-sizing: border-box; }

  html, body {
    width: 849px;
    height: 1200px;
    overflow: hidden;
    background: var(--page-bg);
  }

  .sheet {
    position: relative;
    width: 849px;
    height: 1200px;
    font-family: "PT Sans Narrow", "Arial Narrow", sans-serif;
  }

  .door-sign {
    position: absolute;
    width: 294px;
    height: 215px;
    background: linear-gradient(90deg, #ffffff 51%, var(--tint) 100%);
  }

  .door-sign.level-0 { --level: var(--e0); --tint: var(--e0-tint); left: 50px;  top: 50px; }
  .door-sign.level-1 { --level: var(--e1); --tint: var(--e1-tint); left: 489px; top: 50px; }
  .door-sign.level-2 { --level: var(--e2); --tint: var(--e2-tint); left: 50px;  top: 326px; }
  .door-sign.level-3 { --level: var(--e3); --tint: var(--e3-tint); left: 489px; top: 326px; }
  .door-sign.level-4 { --level: var(--e4); --tint: var(--e4-tint); left: 50px;  top: 603px; }
  .door-sign.level-5 { --level: var(--e5); --tint: var(--e5-tint); left: 489px; top: 603px; }
  .door-sign.level-6 { --level: var(--e6); --tint: var(--e6-tint); left: 50px;  top: 879px; }

  .brand {
    position: absolute;
    left: 9px;
    top: 47px;
    display: flex;
    align-items: center;
    gap: 5px;
    font-weight: 700;
    font-size: 19px;
    letter-spacing: 0.2px;
    color: var(--brand-blue);
    line-height: 1;
  }

  .brand-dot {
    width: 9px;
    height: 9px;
    border-radius: 50%;
    background: var(--brand-blue);
  }

  .level-code {
    position: absolute;
    right: 11px;
    top: 8px;
    font-weight: 700;
    font-size: 44px;
    line-height: 1;
    color: var(--level);
  }

  .level-stripe {
    position: absolute;
    left: 0;
    top: 77px;
    width: 100%;
    height: 8px;
    background: var(--level);
  }

  .resident-name {
    position: absolute;
    left: 0;
    top: 85px;
    width: 100%;
    height: 51px;
    display: flex;
    align-items: center;
    justify-content: center;
    font-weight: 700;
    font-size: 19px;
    color: var(--text-dark);
    white-space: nowrap;
  }

  .room-number {
    position: absolute;
    left: 0;
    top: 136px;
    width: 100%;
    height: 79px;
    display: flex;
    align-items: center;
    justify-content: center;
    background: var(--level);
    color: var(--number-text);
    font-weight: 700;
    font-size: 54px;
    letter-spacing: 1px;
    line-height: 1;
  }
</style>
</head>
<body>
<main class="sheet">

  <article class="door-sign level-0">
    <div class="brand"><span class="brand-dot"></span>BIRKENAU</div>
    <div class="level-code">E0</div>
    <div class="level-stripe"></div>
    <p class="resident-name">Max Mustermann von und zu Birkenau</p>
    <p class="room-number">3028</p>
  </article>

  <article class="door-sign level-1">
    <div class="brand"><span class="brand-dot"></span>BIRKENAU</div>
    <div class="level-code">E1</div>
    <div class="level-stripe"></div>
    <p class="resident-name">Max Mustermann von und zu Birkenau</p>
    <p class="room-number">3028</p>
  </article>

  <article class="door-sign level-2">
    <div class="brand"><span class="brand-dot"></span>BIRKENAU</div>
    <div class="level-code">E2</div>
    <div class="level-stripe"></div>
    <p class="resident-name">Max Mustermann von und zu Birkenau</p>
    <p class="room-number">3028</p>
  </article>

  <article class="door-sign level-3">
    <div class="brand"><span class="brand-dot"></span>BIRKENAU</div>
    <div class="level-code">E3</div>
    <div class="level-stripe"></div>
    <p class="resident-name">Max Mustermann von und zu Birkenau</p>
    <p class="room-number">3028</p>
  </article>

  <article class="door-sign level-4">
    <div class="brand"><span class="brand-dot"></span>BIRKENAU</div>
    <div class="level-code">E4</div>
    <div class="level-stripe"></div>
    <p class="resident-name">Max Mustermann von und zu Birkenau</p>
    <p class="room-number">3028</p>
  </article>

  <article class="door-sign level-5">
    <div class="brand"><span class="brand-dot"></span>BIRKENAU</div>
    <div class="level-code">E5</div>
    <div class="level-stripe"></div>
    <p class="resident-name">Max Mustermann von und zu Birkenau</p>
    <p class="room-number">3028</p>
  </article>

  <article class="door-sign level-6">
    <div class="brand"><span class="brand-dot"></span>BIRKENAU</div>
    <div class="level-code">E6</div>
    <div class="level-stripe"></div>
    <p class="resident-name">Max Mustermann von und zu Birkenau</p>
    <p class="room-number">3028</p>
  </article>

</main>
</body>
</html>
```